Help designing a web admin portal for cloud access control company

Hello, we need help to design our web admin portal for our cloud based access control product called havenpost locks. Please see the attached admin portal wireframe. this is not absolute so we are open to UX / UI suggestions. This web admin portal will allow a admin at a small to medium sized business add new employees to their access control system and grant different access.
Updates

Project Deadline Extended
Reason: Waiting in a couple designs for people that said they would send something in

Target Market(s)

B2B

Industry/Entity Type

It Company

Font styles to use
Sans Serif

Colors
3277b5

Requirements
Must have
• Very simple and clean design. we like clean fonts like Oswald extra light. Please see an image of the wining app designs to see what the color and styling should look like

```html
<!DOCTYPE html>
<html lang="en">
<head>
<meta charset="utf-8">
<title>Havenpost Locks – Dashboard</title>
<link href="https://fonts.googleapis.com/css2?family=Lato:wght@300;400;700&display=swap" rel="stylesheet">
<style>
:root{
  --ink:#222;--muted:#555;--faint:#9a9a9a;--line:#e8e8e8;--bg:#eef2f5;
  --sky:#00b4fb;--sky-dark:#0288c8;--indigo:#5361e6;--purple:#5e35b1;
  --green:#2ecc8f;--red:#f26a6a;--active:#7fd5ff;--badge:#e2463c;
}
*{box-sizing:border-box;margin:0;padding:0}
html,body{width:1200px;height:1200px;overflow:hidden}
body{font-family:'Lato',sans-serif;background:var(--bg);color:var(--ink);position:relative}
.sidebar{position:absolute;left:0;top:0;width:175px;height:1146px;background:#fff}
.brand{position:absolute;left:16px;top:20px;display:flex;flex-direction:column;gap:10px}
.brand-mark{width:38px;height:38px;background:#1e1e1e}
.brand-name{font-size:11.5px;letter-spacing:.5px;font-weight:400}
.menu{position:absolute;top:111px;left:0;width:175px;list-style:none}
.menu li{height:34.3px;display:flex;align-items:center;padding-left:16px;font-size:12px;position:relative}
.menu li .ico{width:11px;height:11px;background:var(--sky);border-radius:2px;margin-right:14px}
.menu li::after{content:"›";position:absolute;right:14px;color:#777;font-size:13px}
.menu li.active{background:var(--active)}
.menu li.active::before{content:"";position:absolute;right:0;top:0;bottom:0;width:4px;background:var(--sky)}
.menu .count{position:absolute;right:30px;width:15px;height:15px;border-radius:50%;background:var(--badge);color:#fff;font-size:9px;display:flex;align-items:center;justify-content:center}
.topbar{position:absolute;left:175px;top:0;right:0;height:49px;background:#fff;border-bottom:1px solid var(--line)}
.topbar .title{position:absolute;left:24px;top:16px;font-size:14px}
.doors{position:absolute;left:183px;top:0;display:flex}
.door{width:77px;height:49px;border-left:1px solid var(--line);display:flex;flex-direction:column;align-items:center;justify-content:center;gap:6px;font-size:9px;color:#333}
.door:last-child{border-right:1px solid var(--line)}
.door i{width:10px;height:14px;background:#3d7fd6;border-radius:1px}
.top-right{position:absolute;right:15px;top:10px;display:flex;align-items:center;gap:18px;font-size:11px;color:#555}
.bell{position:relative;width:14px;height:16px}
.bell b{position:absolute;top:-6px;right:-6px;width:12px;height:12px;border-radius:50%;background:var(--badge);color:#fff;font-size:8px;font-weight:400;display:flex;align-items:center;justify-content:center}
.avatar{width:30px;height:30px;border-radius:50%;background:radial-gradient(circle at 50% 40%,#c99a7f,#6b4a3a)}
.pagehead{position:absolute;left:175px;top:50px;right:0;height:60px;background:#fff}
.pagehead h1{position:absolute;left:23px;top:15px;font-size:20px;font-weight:400}
.stat{position:absolute;top:141px;width:144px;height:93px;color:#fff;display:flex;flex-direction:column;align-items:center;justify-content:center;text-align:center}
.stat strong{font-size:32px;font-weight:300;line-height:1}
.stat span{font-size:11.5px;font-weight:700;margin-top:8px;line-height:1.2}
.panel{position:absolute;background:#fff;box-shadow:0 1px 3px rgba(0,0,0,.05)}
.chart{left:200px;top:260px;width:975px;height:370px}
.chart h2{position:absolute;left:23px;top:24px;font-size:16px;font-weight:400;color:#333}
.select{position:absolute;right:30px;top:23px;height:31px;width:199px;border:1px solid #ddd;border-radius:16px;font-size:12px;color:#555;display:flex;align-items:center;justify-content:center;gap:8px}
.chart svg{position:absolute;left:0;top:0}
.status{left:200px;top:649px;width:478px;height:446px}
.employees{left:697px;top:649px;width:478px;height:446px}
.panel-head{height:42px;border-bottom:1px solid var(--line);padding:13px 22px;font-size:16px;color:#333;position:relative}
.cell{position:absolute;width:239px;display:flex;flex-direction:column;align-items:center}
.ring{width:112px;height:112px;border-radius:50%;border:2px solid #e4e4e4;position:relative;display:flex;align-items:center;justify-content:center}
.ring .flag{position:absolute;right:-4px;bottom:0;width:32px;height:32px;border-radius:50%;display:flex;align-items:center;justify-content:center}
.state{margin-top:20px;font-size:15px;color:#555}
.big{font-size:26px;color:var(--sky);font-weight:400}
.sub{margin-top:20px;font-size:15px;color:#555}
.total{position:absolute;right:17px;top:12px;background:var(--sky);color:#fff;font-size:12px;font-weight:700;padding:3px 6px;border-radius:3px}
.people{list-style:none;position:absolute;left:23px;top:69px}
.people li{height:67px;display:flex;gap:15px}
.face{width:40px;height:40px;border-radius:50%;position:relative;background:radial-gradient(circle at 50% 40%,#d7b096,#5b4032)}
.face.on::after,.face.off::after{content:"";position:absolute;right:-3px;top:0;width:6px;height:6px;border-radius:50%;background:var(--green)}
.face.off::after{background:#aaa}
.who{padding-top:6px;font-size:12.5px;color:#333;line-height:1.25}
.who small{display:block;font-size:12px;color:var(--faint)}
.viewall{position:absolute;left:201px;top:398px;width:76px;height:27px;border-radius:14px;background:#eee;color:#777;font-size:12.5px;display:flex;align-items:center;justify-content:center}
footer{position:absolute;left:0;right:0;top:1146px;height:54px;background:#e4e8ec;display:flex;align-items:center;justify-content:center;font-size:12.5px;color:#333}
</style>
</head>
<body>
<aside class="sidebar">
  <div class="brand"><div class="brand-name" style="font-size:15px;font-weight:700">HAVENPOST</div><div class="brand-name">HAVENPOST LOCKS</div></div>
  <ul class="menu">
    <li><i class="ico"></i>Home</li>
    <li class="active"><i class="ico"></i>Dashboard</li>
    <li><i class="ico"></i>Controller</li>
    <li><i class="ico"></i>Doors</li>
    <li><i class="ico"></i>Employees</li>
    <li><i class="ico"></i>Open/Close Times</li>
    <li><i class="ico"></i>Cameras</li>
    <li><i class="ico"></i>Time Card</li>
    <li><i class="ico"></i>Reports</li>
    <li><i class="ico"></i>Settings<span class="count">2</span></li>
  </ul>
</aside>

<header class="topbar">
  <div class="title">Manual Door Opening</div>
  <nav class="doors">
    <div class="door"><i></i>Main Door</div>
    <div class="door"><i></i>Back Door</div>
    <div class="door"><i></i>Exec Office</div>
    <div class="door"><i></i>Storage Room</div>
  </nav>
  <div class="top-right">
    <svg class="bell" viewBox="0 0 14 16"><path d="M7 1a4 4 0 0 0-4 4v4l-2 3h12l-2-3V5a4 4 0 0 0-4-4zM5.5 13.5a1.5 1.5 0 0 0 3 0" fill="none" stroke="#444" stroke-width="1.2"/></svg>
    <div class="avatar" role="img" aria-label="Admin profile photo"></div>
    <span>⇥ Logout</span>
  </div>
</header>

<div class="pagehead"><h1>Dashboard</h1></div>

<div class="stat" style="left:200px;background:var(--sky)"><strong>28</strong><span>EMPLOYEES</span></div>
<div class="stat" style="left:366px;background:var(--sky)"><strong>24</strong><span>MOBILE ACCESS</span></div>
<div class="stat" style="left:532px;background:var(--indigo)"><strong>75</strong><span>CARD OPENS<br>TODAY</span></div>
<div class="stat" style="left:699px;background:var(--indigo)"><strong>680</strong><span>CARD OPENS<br>MONTH</span></div>
<div class="stat" style="left:865px;background:var(--purple)"><strong>42</strong><span>MOBILE OPENS<br>TODAY</span></div>
<div class="stat" style="left:1031px;background:var(--purple)"><strong>345</strong><span>MOBILE OPENS<br>MONTH</span></div>

<section class="panel chart">
  <h2>Monthly&nbsp; Report</h2>
  <div class="select">Employees &amp; Mobile Access <span>⌄</span></div>
  <svg width="975" height="370" viewBox="0 0 975 370" font-family="Lato,sans-serif" font-size="11" fill="#555">
    <g stroke="#ececec">
      <line x1="50" x2="945" y1="70" y2="70"/><line x1="50" x2="945" y1="110.7" y2="110.7"/>
      <line x1="50" x2="945" y1="151.3" y2="151.3"/><line x1="50" x2="945" y1="192" y2="192"/>
      <line x1="50" x2="945" y1="232.7" y2="232.7"/><line x1="50" x2="945" y1="273.3" y2="273.3"/>
      <line x1="50" x2="945" y1="314" y2="314"/><line x1="50" x2="50" y1="70" y2="314"/><line x1="945" x2="945" y1="70" y2="314"/>
    </g>
    <g text-anchor="end">
      <text x="40" y="74">30</text><text x="40" y="114">25</text><text x="40" y="155">20</text>
      <text x="40" y="196">15</text><text x="40" y="236">10</text><text x="40" y="277">5</text><text x="40" y="318">0</text>
    </g>
    <g fill="#00b4fb">
      <rect x="55" y="192" width="16" height="122"/><rect x="116" y="208.3" width="16" height="105.7"/>
      <rect x="177" y="209.9" width="16" height="104.1"/><rect x="238" y="243.2" width="16" height="70.8"/>
      <rect x="299" y="195.3" width="16" height="118.7"/><rect x="360" y="161.1" width="16" height="152.9"/>
      <rect x="421" y="179" width="16" height="135"/><rect x="482" y="231" width="16" height="83"/>
      <rect x="543" y="204.2" width="16" height="109.8"/><rect x="604" y="123.7" width="16" height="190.3"/>
      <rect x="665" y="161.1" width="16" height="152.9"/><rect x="726" y="157" width="16" height="157"/>
      <rect x="787" y="110.7" width="16" height="203.3"/><rect x="848" y="100.9" width="16" height="213.1"/>
      <rect x="909" y="86.3" width="16" height="227.7"/>
    </g>
    <g fill="#0288c8">
      <rect x="71" y="224.5" width="16" height="89.5"/><rect x="132" y="243.2" width="16" height="70.8"/>
      <rect x="193" y="232.7" width="16" height="81.3"/><rect x="254" y="258.7" width="16" height="55.3"/>
      <rect x="315" y="221.3" width="16" height="92.7"/><rect x="376" y="246.5" width="16" height="67.5"/>
      <rect x="437" y="204.2" width="16" height="109.8"/><rect x="498" y="247.3" width="16" height="66.7"/>
      <rect x="559" y="224.5" width="16" height="89.5"/><rect x="620" y="178.2" width="16" height="135.8"/>
      <rect x="681" y="204.2" width="16" height="109.8"/><rect x="742" y="172.5" width="16" height="141.5"/>
      <rect x="803" y="135.1" width="16" height="178.9"/><rect x="864" y="143.2" width="16" height="170.8"/>
      <rect x="925" y="122.1" width="16" height="191.9"/>
    </g>
    <g text-anchor="middle" font-size="10.5">
      <text x="71" y="337">10/2015</text><text x="132" y="337">11/2015</text><text x="193" y="337">12/2015</text>
      <text x="254" y="337">01/2016</text><text x="315" y="337">02/2016</text><text x="376" y="337">03/2016</text>
      <text x="437" y="337">04/2016</text><text x="498" y="337">05/2016</text><text x="559" y="337">06/2016</text>
      <text x="620" y="337">07/2016</text><text x="681" y="337">08/2016</text><text x="742" y="337">09/2016</text>
      <text x="803" y="337">10/2016</text><text x="864" y="337">11/2016</text><text x="925" y="337">12/2016</text>
    </g>
  </svg>
</section>

<section class="panel status">
  <div class="panel-head">Status</div>
  <div style="position:absolute;left:239px;top:42px;bottom:0;width:1px;background:var(--line)"></div>
  <div style="position:absolute;left:0;right:0;top:242px;height:1px;background:var(--line)"></div>
  <div class="cell" style="left:0;top:67px">
    <div class="ring">
      <svg width="62" height="62" viewBox="0 0 62 62" fill="none" stroke="var(--green)" stroke-width="2">
        <rect x="4" y="4" width="30" height="22" rx="2"/><line x1="19" y1="26" x2="19" y2="32"/><line x1="12" y1="32" x2="26" y2="32"/>
        <circle cx="44" cy="45" r="13"/><path d="M37 40c4 0 6 3 4 6s2 6 6 4M50 34c-2 3 0 6 5 6" /><path d="M38 10h8v4M12 38v10h8" stroke-dasharray="2 2"/>
      </svg>
      <div class="flag" style="background:var(--green)"><svg width="16" height="16" viewBox="0 0 16 16"><path d="M3 8l3.5 3.5L13 5" stroke="#fff" stroke-width="2.5" fill="none"/></svg></div>
    </div>
    <div class="state">Server Status : <span style="color:var(--green)">ON</span></div>
  </div>
  <div class="cell" style="left:239px;top:67px">
    <div class="ring">
      <svg width="62" height="62" viewBox="0 0 62 62" fill="none" stroke="var(--red)" stroke-width="2">
        <rect x="16" y="6" width="24" height="44" rx="4"/><line x1="16" y1="40" x2="40" y2="40"/><circle cx="28" cy="45" r="1.5"/>
        <path d="M24 24a10 10 0 0 1 14 0M27 28a5 5 0 0 1 8 0M21 20a15 15 0 0 1 20 0"/>
      </svg>
      <div class="flag" style="background:var(--red)"><svg width="14" height="14" viewBox="0 0 14 14"><path d="M3 3l8 8M11 3l-8 8" stroke="#fff" stroke-width="2.5"/></svg></div>
    </div>
    <div class="state">Mobile Status : <span style="color:var(--red)">OFF</span></div>
  </div>
  <div class="cell" style="left:0;top:306px"><div class="big">Feb 11, 2016</div><div class="sub">Last Log In</div></div>
  <div class="cell" style="left:239px;top:306px"><div class="big">1</div><div class="sub">Forced Openings</div></div>
</section>

<section class="panel employees">
  <div class="panel-head">Employees<span class="total">28</span></div>
  <ul class="people">
    <li><div class="face on" role="img" aria-label="Employee portrait"></div><div class="who">Maren Holt<small>UI Graphic</small></div></li>
    <li><div class="face on" role="img" aria-label="Employee portrait"></div><div class="who">Tessa Vrane<small>Art director, Movie Cut</small></div></li>
    <li><div class="face" role="img" aria-label="Employee portrait"></div><div class="who">Corinne Ashby<small>Writter, Mag Editor</small></div></li>
    <li><div class="face on" role="img" aria-label="Employee portrait"></div><div class="who">Dorian Pell<small>Designer, Blogger</small></div></li>
    <li><div class="face off" role="img" aria-label="Employee portrait"></div><div class="who">Lila Brandt<small>Writter, Mag Editor</small></div></li>
  </ul>
  <div class="viewall">View All</div>
</section>

<footer>© 2016 Havenpost Locks</footer>
</body>
</html>
```